Modern, Clean, Edgy & Fun Comedy Show Flyer

We need to a create a new flyer for the comedy show, Harbor Laugh Nights. The original version of the flyer is attached (file: Old flyer), as well as two versions of the logo.
- The text should be the same except now the show is Every First Wednesday and the next show is June 1.
- Remove the jerk shop logo
- Remove the picture of the man, and replace it with a photo of Dale (our host), the Audience, or something of your own design.
* pictures of Dale and the Audience is attached.
* We'd like to keep the same color palette and have also attached a color palette for reference

I have also attached 4 references of flyers that I like, that you can use to get an idea of the theme and aesthetic we are looking for.
* Files: Reference 1, Reference 2, Reference 3, Reference 4
Updates

Colors
3277b5
85acd3
0455a3
eaf1f7
cee9f5
ecf7fb
d5d5d5
e6e6e6

Requirements
Must have
• The harbor laugh nights logo attached
• The text as specified in the project description
• An option with Dale and without

```html
<!DOCTYPE html>
<html lang="en">
<head>
<meta charset="utf-8">
<title>Harbor Laugh Nights – Comedy Show Flyer</title>
<link rel="stylesheet" href="https://fonts.googleapis.com/css2?family=Alfa+Slab+One&family=Roboto:wght@700;900&display=swap">
<style>
  :root {
    --sky: #85acd3;
    --sky-deep: #7aa3cc;
    --royal: #0b45d4;
    --navy-splash: #0455a3;
    --splash-light: #3277b5;
    --silver: #c9c9c9;
    --silver-light: #e6e6e6;
    --gold: #b49b5f;
    --ink: #111111;
    --muted: #8a8a8a;
    --paper: #ffffff;
  }
  html, body {
    margin: 0;
    padding: 0;
    overflow: hidden;
    background: var(--paper);
  }
  .flyer {
    position: relative;
    width: 1200px;
    height: 929px;
    overflow: hidden;
    background: var(--paper);
    font-family: "Roboto", Arial, sans-serif;
  }
  .schedule {
    position: absolute;
    top: 26px;
    left: 0;
    width: 100%;
    margin: 0;
    text-align: center;
    font-family: "Roboto", Arial, sans-serif;
    font-weight: 900;
    font-size: 47px;
    letter-spacing: 3px;
    color: var(--sky-deep);
  }
  .splash {
    position: absolute;
    left: 60px;
    top: 100px;
    width: 1090px;
    height: 560px;
  }
  .show-name {
    position: absolute;
    left: 0;
    top: 270px;
    width: 100%;
    margin: 0;
    text-align: center;
    font-family: "Alfa Slab One", Georgia, serif;
    font-weight: 400;
    font-size: 78px;
    line-height: 1.05;
    color: var(--royal);
  }
  .featuring-label {
    position: absolute;
    left: 58px;
    top: 660px;
    margin: 0;
    font-family: "Alfa Slab One", Georgia, serif;
    font-style: italic;
    font-size: 22px;
    color: var(--royal);
  }
  .lineup {
    position: absolute;
    left: 0;
    top: 700px;
    width: 100%;
    height: 60px;
    margin: 0;
    padding: 0;
    list-style: none;
  }
  .comic {
    position: absolute;
    transform: translateX(-50%);
    text-align: center;
    font-family: "Alfa Slab One", Georgia, serif;
    color: var(--gold);
    text-transform: uppercase;
    white-space: nowrap;
  }
  .comic .first { display: block; font-size: 18px; line-height: 22px; }
  .comic .last { display: block; font-size: 30px; line-height: 32px; }
  .host-row {
    position: absolute;
    top: 795px;
    left: 0;
    width: 100%;
    height: 48px;
  }
  .host-label {
    position: absolute;
    left: 271px;
    top: 12px;
    font-weight: 900;
    font-size: 22px;
    letter-spacing: 1px;
    color: var(--sky-deep);
  }
  .host-name {
    position: absolute;
    left: 441px;
    top: 0;
    width: 319px;
    height: 48px;
    line-height: 48px;
    text-align: center;
    background: var(--royal);
    color: var(--paper);
    font-family: "Alfa Slab One", Georgia, serif;
    font-size: 27px;
  }
  .show-date {
    position: absolute;
    left: 782px;
    top: 12px;
    font-weight: 900;
    font-size: 22px;
    letter-spacing: 1px;
    color: var(--sky-deep);
    border-bottom: 2px solid var(--sky-deep);
    line-height: 24px;
  }
  .venue {
    position: absolute;
    left: 0;
    top: 880px;
    width: 100%;
    margin: 0;
    text-align: center;
    font-weight: 700;
    font-size: 19px;
    color: var(--ink);
  }
  .venue .address { color: var(--muted); }
</style>
</head>
<body>
<main class="flyer">
  <h2 class="schedule">COMEDY SHOW EVERY FIRST WEDNESDAY</h2>

  <svg class="splash" viewBox="0 0 1090 560" role="img" aria-label="Distressed silver paint splash with blue spattered edges behind the show name">
    <defs>
      <linearGradient id="silverFill" x1="0" y1="0" x2="1" y2="1">
        <stop offset="0" stop-color="#e6e6e6"/>
        <stop offset="0.5" stop-color="#c4c4c4"/>
        <stop offset="1" stop-color="#d5d5d5"/>
      </linearGradient>
    </defs>
    <path d="M40 120 L120 40 L260 55 L380 10 L520 30 L660 5 L800 35 L940 20 L1050 90 L1075 220 L1060 360 L1080 470 L960 520 L820 545 L660 520 L520 550 L360 530 L220 545 L90 500 L30 400 L10 260 Z" fill="#0455a3" opacity="0.85"/>
    <path d="M60 130 L140 70 L280 80 L400 40 L540 60 L680 35 L820 60 L950 50 L1030 110 L1045 230 L1030 350 L1040 450 L930 490 L800 505 L660 490 L520 515 L370 495 L230 510 L110 470 L55 380 L40 250 Z" fill="url(#silverFill)"/>
  </svg>

  <h1 class="show-name">Harbor Laugh<br>Nights</h1>

  <p class="featuring-label">Featuring</p>
  <ul class="lineup">
    <li class="comic" style="left:153px"><span class="first">Marla</span><span class="last">Benton</span></li>
    <li class="comic" style="left:361px"><span class="first">Owen</span><span class="last">Fairley</span></li>
    <li class="comic" style="left:625px"><span class="first">Noel</span><span class="last">Gardenhurst</span></li>
    <li class="comic" style="left:857px"><span class="first">Ravi</span><span class="last">Mehra</span></li>
    <li class="comic" style="left:1059px"><span class="first">Tina</span><span class="last">Okafor</span></li>
  </ul>

  <div class="host-row">
    <span class="host-label">HOSTED BY</span>
    <span class="host-name">DALE CORBETT</span>
    <span class="show-date">WED. JUNE 1</span>
  </div>

  <p class="venue">The Tin Crate <span class="address">42 Linden Street, Brooklyn</span> Adm: FREE - Doors 6:30 PM</p>
</main>
</body>
</html>
```